VeltaFilez Website

VeltaFiles - Sorted Care Records
We need a Web design for a new company called - VeltaFilez.
VeltaFilez is a Personal Injury and Medical Record Legal Service Outsourcing company. We help Personal Injury Attorneys - with fact based Medical Chronologies and Summaries.

We take Medical Records in disarray and put them in order and summarize them in a chronological order and Update them as needed (if more medical records are added)
Take Releases (for medical records) and work with doctor practices and get the records if needed

Target Market(s)

Personal Injury Attorneys

Industry/Entity Type

Attorney

Number of Pages Required

2 page

Font styles to use
Serif
Sans Serif

Colors

Designer to choose colors to be used in the design.

Requirements
Must have
• Professional Design
• Just need the design for the Home page and Internal pages - I will do the Coding for the pages in html and/or wordpress.
• Don't worry about the content - just need a design.

```html
<!DOCTYPE html>
<html lang="en">
<head>
<meta charset="utf-8">
<title>VeltaFilez – Sorted Care Records</title>
<link rel="stylesheet" href="https://fonts.googleapis.com/css2?family=Lato:ital,wght@0,400;0,700;1,400&family=Raleway:wght@400;700&display=swap">
<style>
:root{
  --navy:#1b4582;
  --navy-dark:#163a6e;
  --ink:#333;
  --footer:#333;
  --bottom:#6f88ab;
  --white:#fff;
  --sans:'Lato',Arial,sans-serif;
  --display:'Raleway',Arial,sans-serif;
}
*{box-sizing:border-box;margin:0;padding:0}
html,body{width:1200px;height:2305px;overflow:hidden;background:var(--white);font-family:var(--sans);color:var(--ink)}
.page{position:relative;width:1200px;height:2305px}
.abs{position:absolute}

/* header */
.brand{left:82px;top:34px;display:flex;align-items:center;gap:12px}
.brand-mark{width:30px;height:30px;background:var(--navy)}
.brand-text{font-family:var(--sans);font-weight:700;font-size:30px;color:var(--navy);letter-spacing:.5px}
.brand-tag{left:82px;top:74px;font-size:11px;color:var(--navy);letter-spacing:1.5px}
.call-icon{left:906px;top:32px;width:52px;height:52px;background:var(--navy);border-radius:3px;display:flex;align-items:center;justify-content:center}
.call-label{left:975px;top:30px;font-size:17px;color:#444}
.call-number{left:975px;top:55px;font-size:21px;font-weight:700;color:var(--navy)}

/* nav */
.nav{left:0;top:115px;width:1200px;height:62px;background:var(--navy)}
.nav-item{top:18px;color:var(--white);font-size:19px}
.nav-sep{top:17px;width:1px;height:28px;background:rgba(255,255,255,.8)}
.search{left:837px;top:13px;width:286px;height:36px;background:var(--white);border-radius:18px;padding:0 14px;display:flex;align-items:center;justify-content:space-between;font-size:14px;color:#666}

/* hero */
.hero{left:0;top:177px;width:1200px;height:600px}
.thumb{width:66px;height:66px;border-radius:50%;border:4px solid var(--white);box-shadow:0 2px 6px rgba(0,0,0,.25)}

/* welcome */
.welcome-title{left:0;top:826px;width:1200px;text-align:center;font-family:var(--display);font-weight:400;font-size:37px;color:#444}
.welcome-title strong,.section-title strong{color:var(--navy);font-weight:700}
.welcome-copy{left:190px;top:893px;width:820px;text-align:center;font-size:13.6px;line-height:25px;color:#666}
.more-btn{left:573px;top:1041px;width:54px;height:54px;border-radius:50%;background:var(--navy);display:flex;align-items:center;justify-content:center}

/* services */
.services{left:0;top:1147px;width:1200px;height:437px;background:linear-gradient(100deg,#5b7db1,#476aa1 45%,#5577ad)}
.section-title{left:0;width:1200px;text-align:center;font-family:var(--display);font-weight:400;font-size:37px}
.services .section-title{top:56px;color:var(--white)}
.services .section-title strong{color:var(--white)}
.service-card{background:rgba(255,255,255,.28);padding:30px 32px;color:var(--white)}
.service-card h3{font-family:var(--display);font-weight:400;font-size:21px;color:#163a6e;line-height:25px;margin-bottom:14px}
.service-card h3 strong{font-weight:700}
.service-card p{font-size:14px;line-height:24px;color:#eef2f8}
.service-card a{display:inline-block;margin-top:12px;font-size:14px;font-weight:700;font-style:italic;color:var(--navy-dark);text-decoration:underline}

/* news */
.news .section-title{top:1640px;color:#333}
.news-card{top:1705px;width:310px;height:260px;padding:36px 0 0 0;box-shadow:8px 0 14px -8px rgba(0,0,0,.12)}
.news-card h4{font-family:var(--display);font-weight:700;font-size:19px;color:var(--navy);margin-bottom:14px}
.news-date{display:flex;align-items:center;gap:10px;font-size:14px;font-style:italic;color:#333;margin-bottom:14px}
.news-card p{font-size:14px;line-height:25px;color:#777;width:290px}

/* footer */
.footer{left:0;top:2012px;width:1200px;height:230px;background:var(--footer);color:var(--white)}
.foot-nav{top:30px;font-size:15px}
.foot-sep{top:32px;width:1px;height:16px;background:#ccc}
.social{top:20px;width:40px;height:40px;border-radius:50%;background:var(--white)}
.social.active{background:#b9c6d9}
.foot-rule{left:0;top:80px;width:1200px;height:1px;background:#666}
.info{top:126px;display:flex;gap:12px;font-size:14px;line-height:24px}
.info-sep{top:124px;width:1px;height:54px;background:#888}
.bottom-bar{left:0;top:2242px;width:1200px;height:63px;background:var(--bottom);color:var(--white);display:flex;align-items:center;justify-content:center;font-size:14px;gap:12px}
</style>
</head>
<body>
<div class="page">

  <div class="abs brand"><span class="brand-mark"></span><span class="brand-text">VeltaFilez</span></div>
  <div class="abs brand-tag">Sorted Care Records</div>

  <div class="abs call-icon">
    <svg width="26" height="26" viewBox="0 0 24 24" fill="#fff"><path d="M6.6 10.8a15 15 0 0 0 6.6 6.6l2.2-2.2a1 1 0 0 1 1-.25 11.4 11.4 0 0 0 3.6.57 1 1 0 0 1 1 1V20a1 1 0 0 1-1 1A17 17 0 0 1 3 4a1 1 0 0 1 1-1h3.5a1 1 0 0 1 1 1c0 1.25.2 2.45.57 3.57a1 1 0 0 1-.25 1z"/></svg>
  </div>
  <div class="abs call-label">Call Us Now</div>
  <div class="abs call-number">(123) 456 0789</div>

  <nav class="abs nav">
    <span class="abs nav-item" style="left:80px">Home</span>
    <span class="abs nav-sep" style="left:162px"></span>
    <span class="abs nav-item" style="left:194px">About</span>
    <span class="abs nav-sep" style="left:278px"></span>
    <span class="abs nav-item" style="left:321px">Services</span>
    <span class="abs nav-sep" style="left:415px"></span>
    <span class="abs nav-item" style="left:456px">News</span>
    <span class="abs nav-sep" style="left:535px"></span>
    <span class="abs nav-item" style="left:568px">Contact</span>
    <div class="abs search">Search....
      <svg width="18" height="18" viewBox="0 0 20 20" fill="none" stroke="#777" stroke-width="2"><circle cx="8" cy="8" r="6"/><path d="M12.5 12.5 18 18"/></svg>
    </div>
  </nav>

  <svg class="abs hero" viewBox="0 0 1200 600" role="img" aria-label="Photo of a motorcycle accident on a roadside with guard rail">
    <defs>
      <linearGradient id="heroFill" x1="0" y1="0" x2="0" y2="1">
        <stop offset="0" stop-color="#4f6a3c"/>
        <stop offset=".2" stop-color="#9aa08d"/>
        <stop offset=".45" stop-color="#c9c7c0"/>
        <stop offset="1" stop-color="#d8d7d3"/>
      </linearGradient>
    </defs>
    <path d="M0 0H1200V478C1010 548 800 575 600 575S190 548 0 478Z" fill="url(#heroFill)"/>
  </svg>
  <div class="abs thumb" role="img" aria-label="Thumbnail photo of an injured person" style="left:482px;top:715px;background:#c8b98a"></div>
  <div class="abs thumb" role="img" aria-label="Thumbnail photo of an accident victim" style="left:565px;top:715px;background:#b7795c"></div>
  <div class="abs thumb" role="img" aria-label="Thumbnail photo of a car collision" style="left:647px;top:715px;background:#8c8f96"></div>

  <h1 class="abs welcome-title">Welcome <strong>VELTAFILEZ</strong></h1>
  <p class="abs welcome-copy">Lorem Ipsum is simply dummy text of the printing and typesetting industry. Lorem Ipsum has been the industry's standard dummy text ever since the 1500s, when an unknown printer took a galley of type and scrambled it to make a type specimen book. It has survived not only five centuries, but also the leap into electronic typesetting, remaining essentially unchanged. It was popularised in the 1960s with the release of Letraset sheets containing Lorem Ipsum passages, and more recently with desktop publishing software like Aldus PageMaker including versions of Lorem Ipsum.</p>
  <div class="abs more-btn">
    <svg width="30" height="20" viewBox="0 0 30 20" fill="none" stroke="#fff" stroke-width="2"><path d="M4 4l11 8 11-8M4 10l11 8 11-8"/></svg>
  </div>

  <section class="abs services" role="img" aria-label="Soft background photo of a doctor with a patient">
    <h2 class="abs section-title">Our <strong>SERVICES</strong></h2>

    <svg class="abs" style="left:0;top:0" width="1200" height="437" viewBox="0 0 1200 437">
      <path d="M456 251H520M680 251H744" stroke="#fff" stroke-width="1.5" opacity=".7"/>
      <polygon points="600,155 684,203 684,299 600,347 516,299 516,203" fill="#1b4582" stroke="#fff" stroke-width="3"/>
      <polygon points="600,170 671,211 671,291 600,332 529,291 529,211" fill="#fff"/>
      <circle cx="410" cy="251" r="46" fill="#1b4582" stroke="#fff" stroke-width="2"/>
      <circle cx="791" cy="251" r="46" fill="#1b4582" stroke="#fff" stroke-width="2"/>
      <g fill="none" stroke="#fff" stroke-width="3">
        <circle cx="410" cy="232" r="9"/>
        <path d="M390 275v-18a14 14 0 0 1 14-14h12a14 14 0 0 1 14 14v18"/>
        <path d="M398 252l14 12"/>
      </g>
      <g fill="none" stroke="#fff" stroke-width="2.5">
        <path d="M791 226v52M775 278h32M771 240h40"/>
        <path d="M771 240l-8 18h16zM811 240l-8 18h16z"/>
      </g>
    </svg>
    <div class="abs" style="left:530px;top:240px;width:140px;text-align:center;font-weight:700;font-size:19px;color:var(--navy)">VeltaFilez</div>

    <div class="abs service-card" style="left:78px;top:156px;width:332px;height:207px;padding-right:60px">
      <h3>Personal <strong>INJURY</strong></h3>
      <p>Lorem Ipsum is simply dummy text of the printing and typesetting of dummy text printing industry.</p>
      <a>READ MORE</a>
    </div>
    <div class="abs service-card" style="left:790px;top:146px;width:332px;height:207px;padding-left:76px">
      <h3>Medical Records <strong>LEGAL SERVICES</strong></h3>
      <p>Lorem Ipsum is simply dummy text of the dummy text printing industry.</p>
      <a>READ MORE</a>
    </div>
  </section>

  <section class="news">
    <h2 class="abs section-title">Latest <strong>NEWS</strong></h2>
    <article class="abs news-card" style="left:79px">
      <h4>Lorem Ipsum is simply dummy</h4>
      <div class="news-date"><svg width="16" height="16" viewBox="0 0 16 16" fill="none" stroke="#333" stroke-width="1.5"><rect x="1.5" y="3" width="13" height="11.5"/><path d="M1.5 6.5h13M5 1v3M11 1v3"/></svg>Posted at 24 / 02 /2018</div>
      <p>Lorem Ipsum is simply dummy text of the printing and typesetting industry. Lorem Ipsum has been the industry's standard .</p>
    </article>
    <article class="abs news-card" style="left:417px">
      <h4>Lorem Ipsum is simply dummy</h4>
      <div class="news-date"><svg width="16" height="16" viewBox="0 0 16 16" fill="none" stroke="#333" stroke-width="1.5"><rect x="1.5" y="3" width="13" height="11.5"/><path d="M1.5 6.5h13M5 1v3M11 1v3"/></svg>Posted at 24 / 02 /2018</div>
      <p>Lorem Ipsum is simply dummy text of the printing and typesetting industry. Lorem Ipsum has been the industry's standard .</p>
    </article>
    <article class="abs news-card" style="left:781px;box-shadow:none">
      <h4>Lorem Ipsum is simply dummy</h4>
      <div class="news-date"><svg width="16" height="16" viewBox="0 0 16 16" fill="none" stroke="#333" stroke-width="1.5"><rect x="1.5" y="3" width="13" height="11.5"/><path d="M1.5 6.5h13M5 1v3M11 1v3"/></svg>Posted at 24 / 02 /2018</div>
      <p>Lorem Ipsum is simply dummy text of the printing and typesetting industry. Lorem Ipsum has been the industry's standard .</p>
    </article>
  </section>

  <footer class="abs footer">
    <span class="abs foot-nav" style="left:79px">Home</span>
    <span class="abs foot-sep" style="left:141px"></span>
    <span class="abs foot-nav" style="left:165px">About</span>
    <span class="abs foot-sep" style="left:227px"></span>
    <span class="abs foot-nav" style="left:252px">Services</span>
    <span class="abs foot-sep" style="left:331px"></span>
    <span class="abs foot-nav" style="left:356px">News</span>
    <span class="abs foot-sep" style="left:414px"></span>
    <span class="abs foot-nav" style="left:439px">Contact</span>

    <span class="abs social active" style="left:926px"></span>
    <span class="abs social" style="left:977px"></span>
    <span class="abs social" style="left:1030px"></span>
    <span class="abs social" style="left:1081px"></span>

    <div class="abs foot-rule"></div>

    <div class="abs info" style="left:77px">
      <svg width="24" height="22" viewBox="0 0 24 22" fill="none" stroke="#fff" stroke-width="1.5"><path d="M1 4l7-3 8 3 7-3v17l-7 3-8-3-7 3zM8 1v17M16 4v17"/></svg>
      <div>VeltaFilez,Inc.<br>Lorem Ipsum is simply dummy<br>printing and typesetting industry</div>
    </div>
    <span class="abs info-sep" style="left:343px"></span>
    <div class="abs info" style="left:405px">
      <svg width="22" height="22" viewBox="0 0 24 24" fill="none" stroke="#fff" stroke-width="1.5"><path d="M6.6 10.8a15 15 0 0 0 6.6 6.6l2.2-2.2a1 1 0 0 1 1-.25 11.4 11.4 0 0 0 3.6.57 1 1 0 0 1 1 1V20a1 1 0 0 1-1 1A17 17 0 0 1 3 4a1 1 0 0 1 1-1h3.5a1 1 0 0 1 1 1c0 1.25.2 2.45.57 3.57a1 1 0 0 1-.25 1z"/></svg>
      <div>(123) 456 0789</div>
    </div>
    <span class="abs info-sep" style="left:608px"></span>
    <div class="abs info" style="left:670px">
      <svg width="20" height="20" viewBox="0 0 20 20" fill="none" stroke="#fff" stroke-width="1.5"><path d="M5 7V1h10v6M3 7h14v8H3zM5 12h10v7H5z"/></svg>
      <div>(123) 456 0789</div>
    </div>
    <span class="abs info-sep" style="left:873px"></span>
    <div class="abs info" style="left:913px">
      <svg width="20" height="16" viewBox="0 0 20 16" fill="none" stroke="#fff" stroke-width="1.5"><rect x="1" y="1" width="18" height="14"/><path d="M1 1l9 8 9-8"/></svg>
      <div>support@veltafilez.com</div>
    </div>
  </footer>

  <div class="abs bottom-bar">
    <span>©</span><span>VeltaFilez Sorted Care Records. - 2018 . All Right Reserved</span>
  </div>

</div>
</body>
</html>
```